The Larchmont Fitters

We need a business card design for our wardrobe company.
Please visit our website www.glimmerbayinteriors.com to get an idea of who we are.

```html
<!DOCTYPE html>
<html lang="en">
<head>
<meta charset="utf-8">
<title>The Larchmont Fitters – Business Card</title>
<link href="https://fonts.googleapis.com/css2?family=Lato:wght@400;700&display=swap" rel="stylesheet">
<style>
  :root {
    --backdrop: #7b4322;
    --card-light: #ffffff;
    --card-dark: #121212;
    --ink: #111111;
    --ink-soft: #3c3c3c;
    --reverse-ink: #ffffff;
  }
  * { box-sizing: border-box; margin: 0; padding: 0; }
  html, body {
    width: 1200px; height: 900px; overflow: hidden;
    background: var(--backdrop);
    font-family: "Lato", Arial, sans-serif;
  }
  .stage { position: relative; width: 1200px; height: 900px; }
  .card {
    position: absolute; left: 330px; width: 558px; height: 343px;
    overflow: hidden;
    box-shadow: 3px 4px 6px rgba(0,0,0,0.45);
  }
  .card--front { top: 90px; background: var(--card-light); }
  .card--back { top: 470px; background: var(--card-dark); }

  .front-accent {
    position: absolute; right: -90px; top: 40px;
    width: 300px; height: 300px; border-radius: 50%;
    background: var(--ink);
  }
  .holder { position: absolute; left: 17px; top: 145px; color: var(--ink-soft); }
  .holder__name {
    font-weight: 700; font-size: 20px; color: var(--ink);
    text-transform: uppercase; line-height: 24px;
  }
  .holder__role { font-size: 16px; line-height: 20px; }
  .address {
    position: absolute; left: 17px; top: 198px;
    font-size: 16px; line-height: 21px; font-style: normal; color: var(--ink-soft);
  }
  .contacts {
    position: absolute; left: 17px; top: 255px; list-style: none;
    font-size: 16px; line-height: 20.5px; color: var(--ink-soft);
  }
  .contacts li { display: flex; align-items: center; gap: 6px; }
  .contacts svg { width: 12px; height: 12px; flex: none; }
  .contacts .icon-fill { fill: var(--ink); }
  .contacts .icon-cut { fill: none; stroke: var(--card-light); stroke-width: 1; }

  .brand {
    position: absolute; left: 130px; top: 141px;
    display: flex; align-items: center; gap: 45px;
    color: var(--reverse-ink);
  }
  .brand__square {
    width: 58px; height: 58px; border: 2px solid var(--reverse-ink); flex: none;
  }
  .brand__text { text-align: center; }
  .brand__name { font-weight: 700; font-size: 18px; line-height: 24px; text-transform: uppercase; }
  .brand__tagline { font-size: 16px; line-height: 24px; }
</style>
</head>
<body>
<main class="stage">
  <section class="card card--front">
    <div class="front-accent"></div>
    <div class="holder">
      <p class="holder__name">Daniel Harrow</p>
      <p class="holder__role">Managing Director</p>
    </div>
    <address class="address">
      Orchard Yard, 42 Fenwick Lane<br>Bristol BS3 7QL
    </address>
    <ul class="contacts">
      <li><svg viewBox="0 0 12 12"><path class="icon-fill" d="M1 4c0-2 2-3 5-3s5 1 5 3l-2 1-1-2H4L3 5zM3 6h6l2 5H1z"/></svg>0117 496 0823</li>
      <li><svg viewBox="0 0 12 12"><path class="icon-fill" d="M1 3h10v7H1z"/><path class="icon-cut" d="M1.5 3.5 6 7l4.5-3.5"/></svg>info@glimmerbayinteriors.com</li>
      <li><svg viewBox="0 0 12 12"><circle class="icon-fill" cx="6" cy="6" r="5.5"/><path class="icon-cut" d="M1 6h10M6 1c-2 3-2 7 0 10M6 1c2 3 2 7 0 10"/></svg>www.glimmerbayinteriors.com</li>
    </ul>
  </section>

  <section class="card card--back">
    <div class="brand">
      <span class="brand__square"></span>
      <div class="brand__text">
        <p class="brand__name">The Larchmont Fitters</p>
        <p class="brand__tagline">Built to Fit Every Room</p>
      </div>
    </div>
  </section>
</main>
</body>
</html>
```